EPIC, awesome, creative business card needed - get involved!

I'm launching a boutique, exclusive Property Management real estate agency in Sydney early next year.
The name of the agency will be called "Silver Oak Lane" - it's a play on "follow the yellow brick road" to wealth. The Silver Oak Lane signifies wealth through property investment.
My business will offer management of investment properties (ie Property Management).
The difference with Silver Oak Lane and other agencies is the business will be run by one of Australia's leading property investment experts, and also one of Australia's leading property managers.
It will be exclusively for high net worth properties and individuals, so the business card needs to be extremely sharp, slick and relatively simple.
The information I want on the card is as follows
Marcus Fenwick - Director
M: 0471 926 154
P: 9637 0518
E: marcus@silveroaklane.net.au
W: silveroaklane.net.au
I'm happy with the red from the logo, black - no yellows or funky colors. I want this to be a super corporate and slick business card to match the high end nature of the business.
Good luck everyone, and please ask questions for clarification.

```html
<!DOCTYPE html>
<html lang="en">
<head>
<meta charset="utf-8">
<title>Silver Oak Lane – Business Card</title>
<link rel="stylesheet" href="https://fonts.googleapis.com/css2?family=Fira+Sans+Extra+Condensed:wght@400;700&family=Figtree:wght@400&display=swap">
<style>
  :root {
    --brand-red: #c01f29;
    --card-text: #ffffff;
    --backdrop: #f0f1f0;
    --note-red: #c01f29;
  }
  html, body {
    margin: 0;
    padding: 0;
    overflow: hidden;
  }
  .canvas {
    position: relative;
    width: 1200px;
    height: 846px;
    background: var(--backdrop);
    overflow: hidden;
    font-family: "Fira Sans Extra Condensed", "Arial Narrow", sans-serif;
  }
  .card-shape {
    position: absolute;
    left: 0;
    top: 0;
    width: 1200px;
    height: 846px;
  }
  .card-shape polygon {
    fill: var(--brand-red);
    filter: drop-shadow(0 1px 2px rgba(0, 0, 0, 0.25));
  }
  .wordmark {
    position: absolute;
    left: 306px;
    top: 178px;
    width: 175px;
    margin: 0;
    color: var(--card-text);
    font-weight: 700;
    font-size: 68px;
    line-height: 96px;
    letter-spacing: 0;
    text-transform: uppercase;
    white-space: nowrap;
  }
  .wordmark span {
    display: block;
  }
  .contact {
    position: absolute;
    left: 654px;
    top: 465px;
    margin: 0;
    padding: 0;
    list-style: none;
    color: var(--card-text);
    font-size: 16px;
    line-height: 19px;
    letter-spacing: 0.7px;
  }
  .contact li {
    display: flex;
    align-items: center;
    gap: 6px;
  }
  .contact .name-line {
    letter-spacing: 1px;
    text-transform: uppercase;
  }
  .contact svg {
    width: 10px;
    height: 10px;
    flex: none;
    fill: var(--card-text);
  }
  .size-note {
    position: absolute;
    left: 76px;
    top: 752px;
    margin: 0;
    color: var(--note-red);
    font-family: "Figtree", "Helvetica", sans-serif;
    font-size: 22px;
  }
</style>
</head>
<body>
<main class="canvas">
  <svg class="card-shape" viewBox="0 0 1200 846" aria-hidden="true">
    <polygon class="card-front" points="260,148 494,148 494,231 575,231 575,525 260,525"/>
    <polygon class="card-back" points="689,227 922,227 922,605 608,605 608,310 689,310"/>
  </svg>

  <h1 class="wordmark">
    <span>Silver</span>
    <span>Oak</span>
    <span>Lane</span>
  </h1>

  <ul class="contact">
    <li class="name-line">Marcus Fenwick / Director</li>
    <li>
      <svg viewBox="0 0 10 10" aria-label="Mobile"><path d="M2 0h6v10H2z M3 1v7h4V1z"/></svg>
      0471 926 154
    </li>
    <li>
      <svg viewBox="0 0 10 10" aria-label="Phone"><path d="M0 3 Q5 0 10 3 L9 5 L7 4 L7 3 L3 3 L3 4 L1 5 Z M2 5 h6 l1 4 H1 Z"/></svg>
      9637 0518
    </li>
    <li>
      <svg viewBox="0 0 10 10" aria-label="Email"><path d="M1 1h8v8H1z M2 2v6h6V2z M4 4h2v2H4z"/></svg>
      marcus@silveroaklane.net.au
    </li>
    <li>
      <svg viewBox="0 0 10 10" aria-label="Website"><circle cx="5" cy="5" r="4.5"/></svg>
      silveroaklane.net.au
    </li>
  </ul>

  <p class="size-note">size: 55 x 65 mm</p>
</main>
</body>
</html>
```